**SUPER EASY AND QUICK - 2 LABELS FOR MASON JAR (JAR AND LID LABEL)

This is going to be a super easy project for someone who can think of a quick great idea!!!! We want to pick a winner really quick, so give us all you got.

I included a sample picture to make it real eazy!!!!

We are filling 8 oz mason jars with CARAMEL POPCORN and dropping them as thank you treats!!!! We need a 2 x 4 label for the base of the jar, and also a 2.5 in circle for lid!!!

We want to have a design with a caramel popcorn border, or caramel popcorn pieces on the labels.

We need to incorporate our logo on the labels also.

We also need the words "We Were Just popping By To Say Thanks!!!"

The font should be something bubbly and fun, like popcorn!!! Not just a plain boring font.

Our company colors are silver and chocolate brown, so we need to incorporate the labels to have colors that match that.
I HAVE UPLOADED A LOT OF STUFF TO MAKE IT EAZY!!!

AGAIN.....SUPER EASY, QUICK AND FUN PROJECT!!!! WE WANT TO PICK A WINNER FAST!!!!

Requirements
Must have
• Popcorn images on the label, our logo and also try to use our colors or colors that match our company colors (silver and chocolate brown). I would like to use "caramel popcorn images", as they look better than regular popcorn images.
• Words "We Were Just Popping By To Say THANKS!!!!"
• Fun Looking Fonts that stand out!!!!
• WE WANT COLORFUL!!!
Should not have
• NO PLAIN FONTS

```html
<!DOCTYPE html>
<html lang="en">
<head>
<meta charset="utf-8">
<title>Popping By Lid Label</title>
<link rel="stylesheet" href="https://fonts.googleapis.com/css2?family=Sniglet:wght@400;800&display=swap">
<style>
  :root {
    --page: #ffffff;
    --caramel-light: #f3d98a;
    --caramel: #d9a644;
    --caramel-deep: #9a6420;
    --ring-cream: #f6e7a6;
    --ring-brown: #5a3422;
    --title-fill: #d6fbf6;
    --title-stroke: #39c8bd;
    --title-shadow: #3b2417;
    --panel: #ffffff;
    --panel-edge: #8d8d8d;
    --brand-brown: #6e3b1c;
  }
  html, body {
    margin: 0;
    padding: 0;
    width: 1198px;
    height: 1200px;
    overflow: hidden;
    background: var(--page);
  }
  .label {
    display: block;
    width: 1198px;
    height: 1200px;
  }
  .headline {
    font-family: "Sniglet", "Comic Sans MS", cursive;
    font-weight: 800;
    font-size: 108px;
    text-anchor: middle;
    letter-spacing: 1px;
  }
  .headline-shadow {
    fill: var(--title-shadow);
    stroke: var(--title-shadow);
    stroke-width: 10px;
    stroke-linejoin: round;
  }
  .headline-face {
    fill: var(--title-fill);
    stroke: var(--title-stroke);
    stroke-width: 3px;
    stroke-linejoin: round;
    paint-order: stroke fill;
  }
  .brand-name, .brand-tagline {
    font-family: "Sniglet", "Comic Sans MS", cursive;
    font-weight: 400;
    fill: var(--brand-brown);
    text-anchor: middle;
  }
  .brand-name { font-size: 74px; }
  .brand-tagline { font-size: 34px; }
</style>
</head>
<body>
<svg class="label" viewBox="0 0 1198 1200" xmlns="http://www.w3.org/2000/svg">
  <defs>
    <radialGradient id="popcorn-tone" cx="50%" cy="45%" r="60%">
      <stop offset="0%" stop-color="var(--caramel-light)"/>
      <stop offset="55%" stop-color="var(--caramel)"/>
      <stop offset="100%" stop-color="var(--caramel-deep)"/>
    </radialGradient>
    <clipPath id="label-edge">
      <circle cx="599" cy="600" r="592"/>
    </clipPath>
  </defs>

  <g clip-path="url(#label-edge)">
    <rect class="popcorn-photo" x="0" y="0" width="1198" height="1200" fill="url(#popcorn-tone)"
          role="img" aria-label="Close-up photograph of caramel popcorn filling the label"/>

    <circle class="inner-ring-cream" cx="599" cy="672" r="488" fill="none" stroke="var(--ring-cream)" stroke-width="14"/>
    <circle class="inner-ring-brown" cx="599" cy="672" r="476" fill="none" stroke="var(--ring-brown)" stroke-width="12"/>

    <g class="headline">
      <text class="headline-shadow" x="604" y="458">We Were Just</text>
      <text class="headline-shadow" x="604" y="586">Popping By</text>
      <text class="headline-shadow" x="604" y="714">To Say Thanks!!</text>
      <text class="headline-face" x="598" y="452">We Were Just</text>
      <text class="headline-face" x="598" y="580">Popping By</text>
      <text class="headline-face" x="598" y="708">To Say Thanks!!</text>
    </g>

    <g class="brand-panel">
      <rect x="270" y="730" width="666" height="420" fill="var(--panel)" stroke="var(--panel-edge)" stroke-width="5"/>
      <text class="brand-name" x="603" y="880">BrightPath</text>
      <text class="brand-name" x="603" y="958">Counseling</text>
      <text class="brand-tagline" x="603" y="1022">a warm caring recovery place</text>
    </g>
  </g>
</svg>
</body>
</html>
```